Real Estate Agent Advertisement

Please create an inviting cohesive postcard advertisement for me. http://www.copperridgerealestate-example.com/ is the website. Please include, name, photo, graphics, phone. Include wholestreet direct mail imprint and addressing. Use mailorbix oversized template size.

Industry/Entity Type

Real Estate Agent

Requirements
Must have
• My name, my photo, name of my broker (company). Company address, my cell phone number and office number.
Nice to have
• Real estate marketing wording. Colors that match look and feel of website. You can look at my agent description and use something out of there as well. Perhaps, SOLD! or something like "Are you looking to buy or sell a home or property? The professional staff at Copper Ridge will make your transaction a success! or Professional marketing of residential, commercial, and Ag property. I am open to ideas for this.

```html
<!DOCTYPE html>
<html lang="en">
<head>
<meta charset="utf-8">
<title>Copper Ridge Postcard</title>
<link rel="stylesheet" href="https://fonts.googleapis.com/css2?family=Oswald:wght@300;500&family=Open+Sans:wght@400;600;700&family=Nothing+You+Could+Do&display=swap">
<style>
  :root {
    --brand-red: #8e1b1e;
    --charcoal: #3b3b3d;
    --panel: #efefef;
    --mid-grey: #a7a8aa;
    --ink: #222222;
    --soft-ink: #3a3a3a;
    --white: #ffffff;
    --page: #e4e4e4;
  }
  * { margin: 0; padding: 0; box-sizing: border-box; }
  html, body { width: 912px; height: 1200px; overflow: hidden; }
  body { background: var(--page); font-family: "Open Sans", sans-serif; position: relative; }

  .postcard { position: absolute; background: var(--white); box-shadow: 0 3px 10px rgba(0,0,0,.25); overflow: hidden; }
  .postcard-front { left: 83px; top: 64px; width: 716px; height: 464px; }
  .postcard-back { left: 127px; top: 650px; width: 717px; height: 464px; }
  .card-art { position: absolute; inset: 0; width: 100%; height: 100%; }

  .brand { position: absolute; display: flex; align-items: center; gap: 10px; }
  .brand-mark { width: 44px; height: 44px; border: 2px solid #9a9a9a; border-radius: 50%; }
  .brand-name { font-weight: 700; font-size: 30px; color: var(--brand-red); letter-spacing: -0.5px; white-space: nowrap; }
  .postcard-front .brand { left: 30px; top: 28px; }
  .postcard-back .brand { left: 18px; top: 30px; }

  .headline { position: absolute; left: 22px; font-family: "Oswald", sans-serif; text-transform: uppercase; font-size: 26px; line-height: 1; letter-spacing: -0.3px; white-space: nowrap; }
  .headline-strong { font-weight: 500; color: var(--ink); }
  .headline-light { font-weight: 300; color: var(--brand-red); }

  .keys-art { position: absolute; left: 215px; top: 314px; width: 150px; height: 72px; border-radius: 6px; background: linear-gradient(135deg, #d8d8d8, #a9a9a9); }

  .contact-bar { position: absolute; left: 0; top: 390px; width: 510px; height: 65px; display: flex; align-items: center; gap: 8px; padding-left: 16px; color: var(--white); font-weight: 700; font-size: 14px; white-space: nowrap; }
  .contact-bar span { flex: none; }
  .contact-bar svg { width: 14px; height: 14px; flex: none; }
  .contact-divider { font-weight: 400; opacity: .8; }

  .listing-banner { position: absolute; font-weight: 600; font-size: 14.5px; white-space: nowrap; }
  .listing-sold { left: 393px; top: 153px; color: var(--soft-ink); }
  .listing-pending { left: 394px; top: 184px; color: var(--white); }

  .partner-badge { position: absolute; left: 270px; width: 116px; background: #d9dbe0; border-radius: 4px; }
  .partner-badge.first { top: 18px; height: 26px; }
  .partner-badge.second { top: 52px; height: 32px; background: #e3dcdc; }

  .history { position: absolute; left: 14px; top: 115px; width: 390px; font-size: 12.5px; line-height: 17.5px; color: var(--soft-ink); }
  .agent-note { position: absolute; left: 13px; top: 187px; width: 420px; font-size: 12.8px; line-height: 20px; color: var(--white); text-align: justify; hyphens: auto; -webkit-hyphens: auto; }
  .signature { position: absolute; left: 300px; top: 322px; font-family: "Nothing You Could Do", cursive; font-size: 24px; color: var(--white); white-space: nowrap; }

  .agent-photo { position: absolute; left: 22px; top: 340px; width: 100px; height: 113px; border: 3px solid var(--white); background: linear-gradient(180deg, #b9b9b9 0%, #8f8f8f 55%, #2f8fd0 56%, #1f78b8 100%); }
  .agent-name { position: absolute; left: 138px; top: 380px; font-size: 13px; color: var(--soft-ink); }
  .agent-details { position: absolute; top: 401px; font-size: 10.5px; line-height: 13.5px; color: var(--soft-ink); white-space: nowrap; }
  .agent-office { left: 138px; }
  .agent-phones { left: 278px; }
</style>
</head>
<body>

<section class="postcard postcard-front">
  <svg class="card-art" viewBox="0 0 716 464" aria-hidden="true">
    <defs>
      <linearGradient id="houseTop" x1="0" y1="0" x2="0" y2="1">
        <stop offset="0" stop-color="#7a6f66"/>
        <stop offset=".45" stop-color="#8a4a36"/>
        <stop offset="1" stop-color="#3f5a2f"/>
      </linearGradient>
      <linearGradient id="houseBottom" x1="0" y1="0" x2="0" y2="1">
        <stop offset="0" stop-color="#6f8a5a"/>
        <stop offset=".35" stop-color="#d2c8b0"/>
        <stop offset=".8" stop-color="#c4bba6"/>
        <stop offset="1" stop-color="#6f8f45"/>
      </linearGradient>
    </defs>
    <rect width="716" height="464" fill="#ffffff"/>
    <rect x="0" y="100" width="420" height="364" fill="var(--panel)"/>
    <rect x="5" y="100" width="340" height="3" fill="#d3d3d3"/>
    <polygon points="333,0 370,0 426,464 402,464" fill="var(--brand-red)"/>
    <polygon points="368,0 716,0 716,207 393,207" fill="url(#houseTop)" role="img" aria-label="Photo of a sold brick cottage with dormers"/>
    <polygon points="393,207 716,207 716,464 424,464" fill="url(#houseBottom)" role="img" aria-label="Photo of a pending-sale house with beige siding"/>
    <rect x="386" y="149" width="330" height="27" fill="rgba(255,255,255,.8)"/>
    <polygon points="380,179 716,179 706,207 383,207" fill="var(--brand-red)"/>
    <rect x="0" y="390" width="510" height="65" fill="var(--charcoal)"/>
  </svg>

  <div class="brand"><span class="brand-mark"></span><span class="brand-name">Copper Ridge</span></div>

  <p class="headline headline-strong" style="top:146px">Professional marketing of</p>
  <p class="headline headline-light" style="top:182px">Residential, commercial</p>
  <p class="headline headline-light" style="top:217px">and agriculture property</p>
  <p class="headline headline-strong" style="top:269px">Thinking about selling?</p>
  <p class="headline headline-light" style="top:305px">Contact us</p>

  <div class="keys-art" role="img" aria-label="House-shaped keychain with a key"></div>

  <span class="listing-banner listing-sold">SOLD!!! 225 South Linden St, Millbrook</span>
  <span class="listing-banner listing-pending">PENDING SALE – 418 S Birch St., Millbrook</span>

  <div class="contact-bar">
    <svg viewBox="0 0 24 24" aria-hidden="true"><path fill="#fff" d="M6.6 10.8a15.1 15.1 0 0 0 6.6 6.6l2.2-2.2a1 1 0 0 1 1-.25 11.4 11.4 0 0 0 3.6.57 1 1 0 0 1 1 1V20a1 1 0 0 1-1 1A17 17 0 0 1 3 4a1 1 0 0 1 1-1h3.5a1 1 0 0 1 1 1c0 1.25.2 2.45.57 3.57a1 1 0 0 1-.25 1z"/></svg>
    <span>555-201-4860</span>
    <span class="contact-divider">|</span>
    <svg viewBox="0 0 24 24" aria-hidden="true"><g fill="none" stroke="#fff" stroke-width="2"><circle cx="12" cy="12" r="9"/><path d="M3 12h18M12 3c3 3 3 15 0 18M12 3c-3 3-3 15 0 18"/></g></svg>
    <span>www.copperridgerealestate-example.com</span>
  </div>
</section>

<section class="postcard postcard-back">
  <svg class="card-art" viewBox="0 0 717 464" aria-hidden="true">
    <rect width="717" height="464" fill="#ffffff"/>
    <polygon points="0,101 470,101 442,175 0,175" fill="var(--mid-grey)"/>
    <polygon points="462,0 492,0 432,175 412,175" fill="#c9c9c9"/>
    <polygon points="455,0 485,0 425,175 405,175" fill="var(--brand-red)"/>
    <polygon points="0,175 438,175 470,362 0,362" fill="var(--charcoal)"/>
    <polygon points="0,362 420,362 500,464 0,464" fill="var(--mid-grey)"/>
    <polygon points="416,362 432,362 505,464 487,464" fill="var(--brand-red)"/>
    <rect x="599.5" y="32.5" width="96" height="78" fill="none" stroke="#c8c8c8"/>
    <g stroke="#cfcfcf" stroke-width="1">
      <line x1="478" y1="187.5" x2="695" y2="187.5"/>
      <line x1="478" y1="219.5" x2="695" y2="219.5"/>
      <line x1="478" y1="252.5" x2="695" y2="252.5"/>
      <line x1="478" y1="285.5" x2="695" y2="285.5"/>
      <line x1="478" y1="317.5" x2="695" y2="317.5"/>
    </g>
  </svg>

  <div class="brand"><span class="brand-mark"></span><span class="brand-name">Copper Ridge</span></div>
  <div class="partner-badge first" aria-label="Listing partner badge"></div>
  <div class="partner-badge second" aria-label="Banking partner badge"></div>

  <p class="history">Copper Ridge Real Estate has been an active force in selling homes, farmland and commercial property in Northeast Nebraska since 1977.</p>

  <p class="agent-note">Thanks for considering me for buying or selling your home or property. I’m a local businessman with farm family roots in the community. I have experience in commercial and residential real estate and property management. Whether you are looking to buy or sell, you can count on me to help you be successful in your next transaction and answer any questions along the way. Call me today!</p>
  <p class="signature">Evan Marsh</p>

  <div class="agent-photo" role="img" aria-label="Headshot of agent Evan Marsh"></div>
  <p class="agent-name">Evan Marsh</p>
  <p class="agent-details agent-office">Office located at:<br>48 N Elm Street<br>Millbrook, NE 68000</p>
  <p class="agent-details agent-phones">Office : 555-201-4100<br>Mobile : 555 380-7720<br>Fax : 555-201-4109</p>
</section>

</body>
</html>
```